Business card for wedding & event planning company

I'm looking for a well designed double sided business card to represent my wedding and event planning company.

It should include the fact we manage the following events:
Weddings, birthdays, conferences, product launches, fashion shows & conventions
in the following areas:
Wiltshire, Oxfordshire, Berkshire & London

My contact details to be included are:

Moira Pennock
07715 482036
moira@amberlarkcelebrations.co.uk
www.amberlarkcelebrations.co.uk

My logo can be found at the following Filevaultex location:
AI file: https://www.filevaultex.com/s/k4mprt8wn31b7hz/brandlogo_sourcefile.ai?dl=0
PNG file:
https://www.filevaultex.com/s/h9qsle2vbx07mnd/brandlogo_image.png?dl=0

Target Market(s)

women aged 30-55

Industry/Entity Type

Wedding

Contact Information for Business Card

in the following areas:

Moira Pennock
Event Planner
07715 482036

Font styles to use
Serif
Sans Serif
Script

Requirements
Must have
• Purple and white colour scheme
Should not have
• Black background
• Please don't submit any of the see-through business card designs.

```html
<!DOCTYPE html>
<html lang="en">
<head>
<meta charset="utf-8">
<title>Amber Lark Celebrations – Business Card</title>
<link rel="stylesheet" href="https://fonts.googleapis.com/css2?family=Cinzel:wght@400&family=Parisienne&display=swap">
<style>
  :root {
    --page: #ffffff;
    --backdrop: #fff6b6;
    --card: #ffffff;
    --purple: #9211a5;
    --purple-light: #c22fd8;
    --purple-ink: #8c1c9e;
    --branch: #a83cbb;
    --white: #ffffff;
    --birthday: #e9b12b;
    --wedding: #4fa2bc;
    --launch: #ec5a62;
    --fashion: #b7a60f;
    --conference: #e7822b;
    --convention: #a89bd1;
  }
  * { box-sizing: border-box; margin: 0; padding: 0; }
  html, body { width: 1200px; height: 900px; overflow: hidden; background: var(--page); }
  .canvas { position: relative; width: 1200px; height: 900px; }
  .backdrop { position: absolute; left: 36px; top: 28px; width: 1128px; height: 844px; background: var(--backdrop); }

  .brand-name {
    font-family: "Cinzel", serif;
    font-weight: 400;
    text-align: center;
    line-height: 1.15;
  }
  .brand-mark {
    display: block;
    margin: 0 auto 10px;
    border-radius: 50%;
    border: 2px solid currentColor;
  }

  .standalone-logo { position: absolute; left: 108px; top: 165px; width: 240px; color: var(--purple-ink); }
  .standalone-logo .brand-mark { width: 70px; height: 70px; }
  .standalone-logo .brand-name { font-size: 28px; }
  .standalone-logo .brand-name small { display: block; font-size: 14px; letter-spacing: 1px; }

  .card { position: absolute; background: var(--card); }
  .card-front { left: 418px; top: 58px; width: 274px; height: 424px; }
  .card-back { left: 730px; top: 225px; width: 388px; height: 603px; }

  .front-panel { position: absolute; left: 16px; top: 15px; width: 242px; height: 330px; background: var(--purple); color: var(--white); }
  .front-panel .standalone { position: absolute; left: 0; top: 95px; width: 100%; }
  .front-panel .brand-mark { width: 64px; height: 64px; }
  .front-panel .brand-name { font-size: 24px; }
  .front-panel .brand-name small { display: block; font-size: 12px; letter-spacing: 1px; }
  .contact-name {
    position: absolute; left: 0; bottom: 6px; width: 100%;
    text-align: center; font-family: "Parisienne", cursive; font-size: 19px;
  }
  .contact-band {
    position: absolute; left: 16px; top: 349px; width: 242px; height: 57px;
    background: var(--purple-light); color: var(--white);
    font-family: "Parisienne", cursive; font-size: 13px;
    padding: 9px 0 0 20px;
  }
  .contact-line { display: flex; align-items: center; gap: 10px; height: 20px; }
  .contact-line svg { flex: none; }

  .back-panel { position: absolute; left: 21px; top: 22px; width: 346px; height: 471px; background: var(--purple); }
  .branches { position: absolute; left: 0; top: 0; }
  .event { position: absolute; width: 110px; text-align: center; }
  .event-icon {
    display: block; width: 104px; height: 104px; margin: 0 auto;
    border-radius: 50%; border: 5px solid var(--white);
  }
  .event-label {
    position: absolute; width: 140px; text-align: center;
    font-family: "Parisienne", cursive; font-size: 21px; line-height: 1.2; color: var(--white);
  }
  .areas-band {
    position: absolute; left: 23px; top: 497px; width: 342px; height: 81px;
    background: var(--purple-light); color: var(--white);
    font-family: "Parisienne", cursive; font-size: 23px; line-height: 1.35;
    text-align: center; padding-top: 10px;
  }
</style>
</head>
<body>
<div class="canvas">
  <div class="backdrop"></div>

  <div class="standalone-logo">
    <span class="brand-mark"></span>
    <p class="brand-name">Amber Lark<small>CELEBRATIONS</small></p>
  </div>

  <section class="card card-front">
    <div class="front-panel">
      <div class="standalone">
        <span class="brand-mark"></span>
        <p class="brand-name">Amber Lark<small>CELEBRATIONS</small></p>
      </div>
      <p class="contact-name">Moira Pennock 07715 482036</p>
    </div>
    <div class="contact-band">
      <p class="contact-line">
        <svg width="14" height="10" viewBox="0 0 14 10"><rect x="0.5" y="0.5" width="13" height="9" fill="none" stroke="#fff"/><path d="M0.5 0.5 L7 6 L13.5 0.5" fill="none" stroke="#fff"/></svg>
        moira@amberlarkcelebrations.co.uk
      </p>
      <p class="contact-line">
        <svg width="12" height="12" viewBox="0 0 12 12"><circle cx="6" cy="6" r="5.5" fill="none" stroke="#fff"/><ellipse cx="6" cy="6" rx="2.5" ry="5.5" fill="none" stroke="#fff"/><line x1="0.5" y1="6" x2="11.5" y2="6" stroke="#fff"/></svg>
        www.amberlarkcelebrations.co.uk
      </p>
    </div>
  </section>

  <section class="card card-back">
    <div class="back-panel">
      <svg class="branches" width="346" height="471" viewBox="0 0 346 471">
        <g fill="none" stroke="var(--branch)" stroke-width="6" stroke-linecap="round">
          <line x1="174" y1="100" x2="174" y2="471"/>
          <line x1="174" y1="300" x2="110" y2="240"/>
          <line x1="174" y1="280" x2="250" y2="210"/>
          <line x1="174" y1="380" x2="110" y2="330"/>
          <line x1="174" y1="410" x2="260" y2="340"/>
        </g>
      </svg>

      <div class="event" style="left:119px;top:22px"><span class="event-icon" role="img" aria-label="Party hat illustration" style="background:var(--birthday)"></span></div>
      <p class="event-label" style="left:104px;top:132px">Birthdays</p>

      <div class="event" style="left:13px;top:125px"><span class="event-icon" role="img" aria-label="Wedding rings illustration" style="background:var(--wedding)"></span></div>
      <p class="event-label" style="left:0;top:238px">Weddings</p>

      <div class="event" style="left:223px;top:125px"><span class="event-icon" role="img" aria-label="Champagne bottle illustration" style="background:var(--launch)"></span></div>
      <p class="event-label" style="left:208px;top:232px">Product<br>launches</p>

      <div class="event" style="left:119px;top:200px"><span class="event-icon" role="img" aria-label="Dress illustration" style="background:var(--fashion)"></span></div>
      <p class="event-label" style="left:104px;top:318px">Fashion<br>shows</p>

      <div class="event" style="left:30px;top:322px"><span class="event-icon" role="img" aria-label="Suit and tie illustration" style="background:var(--conference)"></span></div>
      <p class="event-label" style="left:15px;top:432px">Conferences</p>

      <div class="event" style="left:211px;top:322px"><span class="event-icon" role="img" aria-label="Group of people illustration" style="background:var(--convention)"></span></div>
      <p class="event-label" style="left:196px;top:432px">Conventions</p>
    </div>
    <div class="areas-band">London, Oxfordshire,<br>Berkshire &amp; Wiltshire</div>
  </section>
</div>
</body>
</html>
```